Coral Bay Dental Surgery Business Cards

Hi there

Can i please have a simple business card designed (front and back with a black background) using out white reverse logo and the same font used for the logo?
On the back we can just have the logo. Full details at the front part.
Here are the details:

Name of the surgery: Coral Bay | Dental Surgery
Name on the business card: Dr Owen Thackery
Credentials:
BDSc (KTL)
MSc Oral Implantology (Halvorsen, Frankfurt)
Fellow & Diplomate (Meridian Council of Restorative Prosthetics)

Email: owen.thackery@coralbaysmile.example
Address: 17 Lisgrove Rd Karrinyup
Website: coralbaysmile.example
Phone: 1800 316 482

We have attached our high res logo and a rudimentary version of the business card which is not necessarily what we want but gives all the details
We would like to have the print ready version. Thanks.

Contact Information for Business Card

website. credentials. qr code. address. phone number

Requirements
Must have
• QR code

```html
<!DOCTYPE html>
<html lang="en">
<head>
<meta charset="utf-8">
<title>Coral Bay Dental Surgery – Business Card</title>
<link rel="stylesheet" href="https://fonts.googleapis.com/css2?family=Montserrat:wght@400;500;600;700&display=swap">
<style>
  :root {
    --backdrop: #808080;
    --paper: #ffffff;
    --ink: #1c1c1c;
    --night: #0b0b0b;
    --teal: #0aa79e;
    --blue: #0bb0ea;
    --accent: #12a3c6;
  }
  * { box-sizing: border-box; margin: 0; padding: 0; }
  html, body {
    width: 1200px; height: 1200px; overflow: hidden;
    background: var(--backdrop);
    font-family: "Montserrat", sans-serif;
  }
  .card {
    position: absolute;
    left: 141px;
    width: 919px;
    height: 524px;
    overflow: hidden;
  }
  .card--front { top: 60px; background: var(--paper); }
  .card--back { top: 616px; background: var(--night); }

  .edge-bar {
    position: absolute; left: 0; top: 0;
    width: 47px; height: 268px;
    background: linear-gradient(180deg, var(--teal) 0%, var(--blue) 100%);
  }
  .doctor-name {
    position: absolute; left: 78px; top: 66px;
    font-size: 34px; font-weight: 600;
    color: var(--accent);
    letter-spacing: 0.2px;
  }
  .credentials {
    position: absolute; left: 78px; top: 125px;
    font-size: 20px; font-weight: 400; line-height: 27px;
    color: var(--ink);
  }
  .credentials p + p { margin-top: 25px; }

  .contact-list {
    position: absolute; left: 78px; top: 326px;
    list-style: none;
  }
  .contact-list li {
    display: flex; align-items: center;
    height: 36px;
    font-size: 23px; font-weight: 400; color: var(--ink);
  }
  .contact-list svg {
    width: 18px; height: 18px; margin-right: 20px; flex: none;
    fill: var(--accent);
  }

  .brand-art {
    position: absolute; right: 0; top: 0;
    width: 300px; height: 100%;
    background: linear-gradient(200deg, rgba(11,176,234,0.16) 0%, rgba(10,167,158,0.08) 60%, rgba(255,255,255,0) 100%);
  }
  .qr-code {
    position: absolute; right: 56px; bottom: 52px;
    width: 150px; height: 150px;
    background: var(--paper);
    border: 10px solid var(--ink);
    outline: 6px solid var(--paper);
  }

  .brand-name {
    position: absolute; left: 0; right: 0; top: 240px;
    display: flex; align-items: center; justify-content: center; gap: 22px;
    color: #ffffff;
    font-size: 38px; font-weight: 500;
    letter-spacing: 4px;
  }
  .brand-name .dot {
    width: 26px; height: 26px; border-radius: 50%;
    background: var(--accent);
  }
</style>
</head>
<body>
  <section class="card card--front" aria-label="Business card front">
    <div class="edge-bar"></div>
    <h1 class="doctor-name">Dr. Owen Thackery</h1>
    <div class="credentials">
      <p>BDSc (KTL)<br>MSc Oral Implantology (Halvorsen, Frankfurt)</p>
      <p>Fellow &amp; Diplomate<br>(Meridian Council of Restorative Prosthetics)</p>
    </div>
    <ul class="contact-list">
      <li>
        <svg viewBox="0 0 16 16" aria-hidden="true"><path d="M4 0h8a1.5 1.5 0 0 1 1.5 1.5v13A1.5 1.5 0 0 1 12 16H4a1.5 1.5 0 0 1-1.5-1.5v-13A1.5 1.5 0 0 1 4 0zm0 2v10.5h8V2zm4 11.2a.9.9 0 1 0 0 1.8.9.9 0 0 0 0-1.8z"/></svg>
        1800 316 482
      </li>
      <li>
        <svg viewBox="0 0 16 16" aria-hidden="true"><path d="M0 3h16v10H0zm1.5 1.4v.3L8 9l6.5-4.3v-.3z"/></svg>
        owen.thackery@coralbaysmile.example
      </li>
      <li>
        <svg viewBox="0 0 16 16" aria-hidden="true"><path d="M8 0a8 8 0 1 0 0 16A8 8 0 0 0 8 0zm0 1.5c.8 0 1.9 1.9 2.2 5H5.8C6.1 3.4 7.2 1.5 8 1.5zM5.8 8h4.4c-.3 3.1-1.4 6.5-2.2 6.5S6.1 11.1 5.8 8zm-1.5 0c.1 2.3.7 4.4 1.5 5.8A6.5 6.5 0 0 1 1.5 8zm7.4 0h2.8a6.5 6.5 0 0 1-4.3 5.8c.8-1.4 1.4-3.5 1.5-5.8zm0-1.5c-.1-2.3-.7-4.4-1.5-5.8a6.5 6.5 0 0 1 4.3 5.8zm-7.4 0H1.5a6.5 6.5 0 0 1 4.3-5.8c-.8 1.4-1.4 3.5-1.5 5.8z"/></svg>
        www.coralbaysmile.example
      </li>
      <li>
        <svg viewBox="0 0 16 16" aria-hidden="true"><path d="M8 0a5.5 5.5 0 0 0-5.5 5.5C2.5 9.6 8 16 8 16s5.5-6.4 5.5-10.5A5.5 5.5 0 0 0 8 0zm0 7.6a2.1 2.1 0 1 1 0-4.2 2.1 2.1 0 0 1 0 4.2z"/></svg>
        17 Lisgrove Rd Karrinyup
      </li>
    </ul>
    <div class="brand-art" role="img" aria-label="Large decorative brand symbol in teal and blue"></div>
    <div class="qr-code" role="img" aria-label="QR code linking to the surgery website"></div>
  </section>

  <section class="card card--back" aria-label="Business card back">
    <div class="brand-name">
      <span class="dot"></span>
      <span>Coral Bay Dental Surgery</span>
    </div>
  </section>
</body>
</html>
```